Coastal Body Remedies business is seeking a Business Card Design

We are a new natural therapy business that needs a Business Card Design with an appointment card on the back.

We offer Myotherapy (muscle therapy) services and have a strong focus and commitment to helping people relieve pain and restore movement to their bodies.

I am attaching my business logo for you information.

Business card must contain my logo and have space for name, title, qualifications, phone number, email, web address

Appointment Card on the back of the card must contain space to write next appointment date, time and name of therapist and cancellation policy.

Cancellation Policy
Minimum of 24hrs notice is required prior to appointment time or full treatment fees with apply.

```html
<!DOCTYPE html>
<html lang="en">
<head>
<meta charset="utf-8">
<title>Coastal Body Remedies – Appointment Card</title>
<link href="https://fonts.googleapis.com/css2?family=Quicksand:wght@400;500;700&display=swap" rel="stylesheet">
<style>
  :root {
    --green: #86bc3e;
    --ink: #2b2b2b;
    --brown: #5a4a40;
    --paper: #fbfbfb;
    --rule: #2e2a27;
    --white: #ffffff;
  }
  * { margin: 0; padding: 0; box-sizing: border-box; }
  html, body { width: 1200px; height: 724px; overflow: hidden; background: var(--white); }
  .card {
    position: relative;
    width: 1200px; height: 724px;
    background: var(--paper);
    border-top: 3px solid var(--rule);
    border-bottom: 3px solid var(--rule);
    font-family: "Quicksand", sans-serif;
    color: var(--ink);
  }
  .label-band {
    position: absolute;
    background: var(--green);
    color: var(--white);
    font-weight: 700;
    text-transform: uppercase;
    display: flex; align-items: center; justify-content: center;
  }
  .label-band--next { left: 66px; top: 58px; width: 453px; height: 53px; font-size: 36px; letter-spacing: 2px; }
  .label-band--policy { left: 66px; top: 487px; width: 392px; height: 45px; font-size: 27px; letter-spacing: 1.6px; }

  .field {
    position: absolute;
    display: flex; align-items: baseline;
    font-size: 27px; font-weight: 500; letter-spacing: 1px;
    text-transform: uppercase;
  }
  .field__line {
    display: inline-block;
    height: 4px;
    margin-left: 6px;
    background-image: radial-gradient(circle, var(--ink) 1.2px, transparent 1.5px);
    background-size: 6px 4px;
    background-repeat: repeat-x;
  }
  .field--date { left: 67px; top: 180px; }
  .field--date .field__line { width: 312px; }
  .field--time { left: 510px; top: 180px; }
  .field--time .field__line { width: 215px; }
  .field--therapist { left: 67px; top: 384px; }
  .field--therapist .field__line { width: 690px; }

  .choice {
    position: absolute;
    display: flex; align-items: center; gap: 8px;
    font-size: 29px; font-weight: 500; letter-spacing: 1px;
  }
  .choice__box {
    display: inline-block;
    border: 4px solid var(--green);
    border-radius: 7px;
    background: var(--white);
  }
  .choice--meridiem .choice__box { width: 43px; height: 36px; }
  .choice--day .choice__box { width: 49px; height: 48px; }
  .choice--am { left: 860px; top: 179px; }
  .choice--pm { left: 993px; top: 179px; }

  .days { position: absolute; top: 275px; left: 0; }
  .days .choice { top: 0; }

  .policy-text {
    position: absolute; left: 67px; top: 548px;
    font-size: 27px; line-height: 42px; letter-spacing: 1.4px;
    font-weight: 500;
  }

  .brand {
    position: absolute; left: 654px; top: 521px;
    width: 443px; height: 139px;
    display: flex; align-items: center; gap: 22px;
  }
  .brand__mark { width: 110px; height: 110px; background: var(--green); flex: none; }
  .brand__name {
    font-family: "Quicksand", sans-serif;
    font-weight: 700; font-size: 34px; line-height: 40px;
    color: var(--brown); letter-spacing: 0.5px;
  }
</style>
</head>
<body>
  <main class="card">
    <div class="label-band label-band--next">Next Appointment</div>

    <div class="field field--date">Date:<span class="field__line"></span></div>
    <div class="field field--time">Time:<span class="field__line"></span></div>
    <div class="choice choice--meridiem choice--am">AM<span class="choice__box"></span></div>
    <div class="choice choice--meridiem choice--pm">PM<span class="choice__box"></span></div>

    <div class="days">
      <div class="choice choice--day" style="left:74px">Mon<span class="choice__box"></span></div>
      <div class="choice choice--day" style="left:229px">Tue<span class="choice__box"></span></div>
      <div class="choice choice--day" style="left:378px">Wed<span class="choice__box"></span></div>
      <div class="choice choice--day" style="left:541px">Thu<span class="choice__box"></span></div>
      <div class="choice choice--day" style="left:688px">Fri<span class="choice__box"></span></div>
      <div class="choice choice--day" style="left:816px">Sat<span class="choice__box"></span></div>
      <div class="choice choice--day" style="left:958px">Sun<span class="choice__box"></span></div>
    </div>

    <div class="field field--therapist">Name of Therapist:<span class="field__line"></span></div>

    <div class="label-band label-band--policy">Cancellation Policy</div>
    <p class="policy-text">Minimum of 24hrs notice is required<br>prior to appointment time or full<br>treatment fees will apply</p>

    <div class="brand">
      <span class="brand__mark"></span>
      <span class="brand__name">Coastal Body<br>Remedies</span>
    </div>
  </main>
</body>
</html>
```